Brochure Design Project

Looking for 8.5 x 5.5 brochure for new indoor cycling studio. This will be the first upscale, boutique indoor cycling studio in our area. Our studio will be decorated in modern grays and whites with pops of orange and blue. Looking to incorporate the image of oranges in clear cylinders on the front, and then it exploding on the back. Open to other ideas. Looking for modern and fresh.
Logo attached. Copy below.
"Are you ready to Velmo? Bring It."
"Velmo Indoor Cycling Studio is a state of the art boutique cycling studio located in the Harlow Sports Center in Ashby Meadows.
The Studio offers cycling fitness programs for everyone from beginners to seasoned indoor cyclists. By incorporating best in class bikes, technology and facilities, Velmo Indoor Cycling Studio sets the standard in indoor cycling."
"What we Bring:
-State of the art online reservation system
-Top of the Line Bikes that are specially tuned for optimum performance
-Stadium Seating. Premium Sound. Smart Lighting.
-High energy certified instructors
-The best customer service....Period."
"Come take a Velmo!"
2281 Penwick Lane
Brentwood, TN 37027
615.555.0192
velmospin.example

```html
<!DOCTYPE html>
<html lang="en">
<head>
<meta charset="utf-8">
<title>Velmo Brochure – Inside Spread</title>
<link href="https://fonts.googleapis.com/css2?family=Jost:wght@700;800&family=Arimo:wght@400&display=swap" rel="stylesheet">
<style>
  :root {
    --orange: #f26a24;
    --blue: #0a7bb8;
    --grey: #bcbdbf;
    --banner-grey: #a7a9ac;
    --text-grey: #6d6e71;
    --paper: #ffffff;
    --backdrop: #f1f1f1;
    --bike-peach: #fbe3d3;
    --bike-grey: #ececec;
  }
  * { margin: 0; padding: 0; box-sizing: border-box; }
  html, body { width: 1200px; height: 900px; overflow: hidden; }
  body { background: var(--backdrop); position: relative; font-family: "Arimo", Arial, sans-serif; }

  .spread {
    position: absolute; left: 220px; top: 156px;
    width: 760px; height: 588px;
    display: flex; background: var(--paper);
    box-shadow: 0 6px 24px rgba(0,0,0,0.12);
  }
  .page { position: relative; width: 380px; height: 100%; overflow: hidden; z-index: 1; }
  .page--left { border-left: 20px solid var(--grey); }
  .page--right { border-right: 20px solid var(--orange); }

  .page__header {
    height: 130px; display: flex; align-items: flex-end;
    padding: 0 24px 22px;
  }
  .page--left .page__header { background: var(--orange); }
  .page--right .page__header { background: var(--blue); padding-bottom: 60px; }
  .page__title {
    font-family: "Jost", "Futura", sans-serif; font-weight: 800;
    font-size: 33px; color: var(--paper); letter-spacing: 0.2px;
  }

  .about { padding: 22px 24px 0; color: var(--text-grey); font-size: 13px; line-height: 1.55; width: 230px; }
  .about p + p { margin-top: 18px; }

  .bring-list { list-style: none; padding: 14px 24px 0 32px; color: var(--text-grey); font-size: 12px; line-height: 1.45; }
  .bring-list li { position: relative; }
  .bring-list li::before {
    content: ""; position: absolute; left: -14px; top: 6px;
    width: 4px; height: 4px; border-radius: 50%; background: var(--orange);
  }

  .bike-art {
    position: absolute; left: 20px; right: 20px; bottom: 0; height: 340px;
    background: linear-gradient(90deg, var(--bike-peach) 0%, var(--bike-grey) 45%, var(--bike-grey) 60%, var(--bike-peach) 100%);
    opacity: 0.45; z-index: 0;
  }

  .tagline { position: absolute; left: 22px; top: 322px; width: 338px; height: 100px; }
  .tagline__mark {
    position: absolute; left: 0; top: -20px;
    font-family: "Jost", sans-serif; font-weight: 800; font-size: 66px;
    color: var(--orange); line-height: 1;
  }
  .tagline__banner { position: absolute; left: 26px; top: 36px; width: 312px; height: 56px; }
  .tagline__text {
    position: absolute; left: 50px; top: 44px;
    font-family: "Jost", sans-serif; font-weight: 800; font-size: 24px;
    color: var(--paper); white-space: nowrap;
  }
</style>
</head>
<body>
  <div class="spread">
    <div class="bike-art" role="img" aria-label="Faint outline illustration of a bicycle spanning both pages"></div>

    <section class="page page--left">
      <header class="page__header"><h2 class="page__title">About Us:</h2></header>
      <div class="about">
        <p>Velmo Indoor Cycling Studio is a state of the art boutique cycling studio located in the Harlow Sports Center in Ashby Meadows.</p>
        <p>The Studio offers cycling fitness programs for everyone from beginners to seasoned indoor cyclists. By incorporating best in class bikes, technology and facilities, Velmo Indoor Cycling Studio sets the standard in indoor cycling.</p>
      </div>
    </section>

    <section class="page page--right">
      <header class="page__header"><h2 class="page__title">What We Bring:</h2></header>
      <ul class="bring-list">
        <li>State of the art online reservation system</li>
        <li>Top of the Line Bikes that are specially tuned for optimum performance</li>
        <li>Stadium Seating. Premium Sound. Smart Lighting.</li>
        <li>High energy certified instructors</li>
        <li>The best customer service....Period.</li>
      </ul>

      <div class="tagline">
        <span class="tagline__mark">“</span>
        <svg class="tagline__banner" viewBox="0 0 312 56" aria-hidden="true">
          <polygon points="0,0 312,0 312,56 16,56 16,24 0,12" fill="var(--banner-grey)"/>
        </svg>
        <span class="tagline__text">Come Take A Velmo!”</span>
      </div>
    </section>
  </div>
</body>
</html>
```